Business Card Design

I need a card design for Melbourne based business in Australia, called T W Concrete Services. We Concrete and excavate. Concreteing is main part of business.Commercial ,Residential and industrial.We want to be known as T W C (services) as form of abbreviation.We would like to highlight the initials with contact phone. A clean straight edge design. We have no color preference and would prefer a design that can easily be used on all parts of our business including clothing,vechiles and stationary

Industry/Entity Type

Business

Contact Information for Business Card

Colin 0412 905 268
Barry 0421 574 360
twcsercices@quokkanet.com

```html
<!DOCTYPE html>
<html lang="en">
<head>
<meta charset="utf-8">
<title>T W Concrete Services – Business Card</title>
<link rel="stylesheet" href="https://fonts.googleapis.com/css2?family=Titillium+Web:wght@600;700&display=swap">
<style>
  :root {
    --page-bg: #e9e7e3;
    --concrete-light: #c2c5c6;
    --concrete-dark: #a7abad;
    --panel-white: #ffffff;
    --brand-blue: #0f5878;
    --ink: #111418;
  }
  * { margin: 0; padding: 0; box-sizing: border-box; }
  html, body {
    width: 1200px;
    height: 1200px;
    overflow: hidden;
    background: var(--page-bg);
  }
  .canvas {
    position: relative;
    width: 1200px;
    height: 1200px;
  }
  .business-card {
    position: absolute;
    left: 60px;
    top: 267px;
    width: 1080px;
    height: 665px;
    overflow: hidden;
    box-shadow: 0 4px 14px rgba(0,0,0,0.18);
  }
  .concrete-surface {
    position: absolute;
    inset: 0;
    background: linear-gradient(160deg, var(--concrete-light) 0%, #b6b9ba 55%, var(--concrete-dark) 100%);
  }
  .header-panel {
    position: absolute;
    inset: 0;
    width: 100%;
    height: 100%;
  }
  .brand-name {
    position: absolute;
    right: 70px;
    top: 70px;
    font-family: "Titillium Web", sans-serif;
    font-weight: 700;
    color: var(--brand-blue);
    text-align: right;
    line-height: 0.9;
    text-transform: uppercase;
  }
  .brand-initials {
    display: block;
    font-size: 132px;
    letter-spacing: 4px;
  }
  .brand-words {
    display: block;
    font-size: 44px;
    letter-spacing: 1px;
    margin-top: 6px;
  }
  .contact-list {
    position: absolute;
    left: 60px;
    top: 360px;
    font-family: "Titillium Web", sans-serif;
    font-weight: 700;
    color: var(--ink);
    font-size: 29px;
    list-style: none;
  }
  .contact-line {
    display: flex;
    align-items: center;
    height: 52px;
  }
  .contact-icon {
    width: 28px;
    height: 28px;
    margin-right: 14px;
    fill: var(--ink);
  }
  .contact-email { font-weight: 600; }
</style>
</head>
<body>
<div class="canvas">
  <section class="business-card">
    <div class="concrete-surface" role="img" aria-label="Grey poured concrete surface texture"></div>

    <svg class="header-panel" viewBox="0 0 1080 665" preserveAspectRatio="none" aria-hidden="true">
      <polygon class="panel-white" fill="var(--panel-white)" points="380,0 1080,0 1080,270 760,440"/>
    </svg>

    <h1 class="brand-name">
      <span class="brand-initials">T W</span>
      <span class="brand-words">Concrete Services</span>
    </h1>

    <ul class="contact-list">
      <li class="contact-line contact-person">Colin</li>
      <li class="contact-line">
        <svg class="contact-icon" viewBox="0 0 24 24" aria-hidden="true"><path d="M6.6 10.8a15.1 15.1 0 0 0 6.6 6.6l2.2-2.2a1 1 0 0 1 1-.25 11.4 11.4 0 0 0 3.6.57 1 1 0 0 1 1 1V20a1 1 0 0 1-1 1A17 17 0 0 1 3 4a1 1 0 0 1 1-1h3.5a1 1 0 0 1 1 1c0 1.25.2 2.45.57 3.57a1 1 0 0 1-.25 1z"/></svg>
        0412 905 268
      </li>
      <li class="contact-line contact-person">Barry</li>
      <li class="contact-line">
        <svg class="contact-icon" viewBox="0 0 24 24" aria-hidden="true"><path d="M6.6 10.8a15.1 15.1 0 0 0 6.6 6.6l2.2-2.2a1 1 0 0 1 1-.25 11.4 11.4 0 0 0 3.6.57 1 1 0 0 1 1 1V20a1 1 0 0 1-1 1A17 17 0 0 1 3 4a1 1 0 0 1 1-1h3.5a1 1 0 0 1 1 1c0 1.25.2 2.45.57 3.57a1 1 0 0 1-.25 1z"/></svg>
        0421 574 360
      </li>
      <li class="contact-line contact-email">
        <svg class="contact-icon" viewBox="0 0 24 24" aria-hidden="true"><path d="M2 5h20v14H2z M4 7v.4l8 5.2 8-5.2V7z M4 9.8V17h16V9.8l-8 5.2z" fill-rule="evenodd"/></svg>
        twcsercices@quokkanet.com
      </li>
    </ul>
  </section>
</div>
</body>
</html>
```